Premium Corporate Website Design for Velmora Systems

Our company Velmora Systems GmbH (formerly BrightHarbor GmbH) is looking for a new, modern, and professional corporate website. The content should be based on our existing site bright-harbor.example
, but reimagined in a contemporary, tech-oriented, and premium design.

Requirements:

- Alignment with the new Velmora Systems logo and corporate identity
- Modern layout that reflects the tech and IT consulting industry
- Clear and user-friendly structure with intuitive navigation
- Premium look and feel that highlights our market position
- Incorporation of animated or interactive elements to add dynamism
- Design should clearly stand out from competitors such as Durlak GmbH, TMPulse, Vorndal, Marvix, and Holtreuven
- International focus: Since our company also operates in the U.S. market, the website should reflect a global presence (e.g., bilingual structure in German/English, international visual language, U.S.-inspired corporate design elements)

Goal:
To create a high-quality, innovative, and brand-strong website that positions Velmora Systems GmbH as a modern, trustworthy, and future-oriented IT consulting company — both in the German-speaking region and in the United States.

In addition to the design, we would also like the website to be delivered as functional HTML/CSS files (or WordPress implementation if possible).

All images from our current website www.bright-harbor.example
can be used if needed. Designers are welcome to reuse or adapt this material where appropriate."

Target Market(s)

Medium to large enterprises in the technology, finance, and energy sectors Companies seeking premium IT consulting, quality assurance, and test automation services Decision makers and executives (CIOs, CTOs, IT managers) in Europe and the United States A global audience that values innovation, professionalism, and trust

Industry/Entity Type

Information Technology & Consulting Software Testing & Quality Assurance Technology / Professional Services

Coding

Number of Pages Required

Requirements
Must have
• - Integration of the Velmora Systems logo and corporate identity - Bilingual setup (German & English) Modern, premium tech design with a professional look and feel Clear structure and intuitive navigation for easy usability Responsive design, optimized for desktop, tablet, and mobile High-quality visuals and dynamic elements (animations, interactive features) Strong differentiation from competitors (Durlak GmbH, TMPulse, Vorndal, Marvix, Holtreuven)
Nice to have
• Subtle micro-animations and hover effects to enhance user experience Custom icons or illustrations that align with the Velmora brand Dark/Light mode toggle for modern usability Blog or insights section to share expertise and updates SEO-friendly structure for better visibility in search engines Integration of social media feeds (LinkedIn, Facebook, Instagram) Contact form with automation (e.g., PHPMailer or CRM integration) Showcasing case studies or success stories with an engaging layout
Should not have
• Overly crowded or cluttered layouts Stock images that look generic or low quality Outdated design styles (e.g., gradients from the 2000s, heavy drop shadows) Complex navigation that confuses users Excessive use of bright or non-brand colors outside the Velmora identity Long loading times caused by oversized media files Pop-ups or intrusive ads that disrupt the premium brand image

```html
<!DOCTYPE html>
<html lang="en">
<head>
<meta charset="utf-8">
<title>Velmora Systems GmbH</title>
<link href="https://fonts.googleapis.com/css2?family=Krona+One&family=Roboto:wght@400;500;700&display=swap" rel="stylesheet">
<style>
:root{
  --green:#3fe21e;
  --blue:#0a55e6;
  --navy:#0b1a3a;
  --ink:#0f2145;
  --text:#5a5f6b;
  --field:#efeff1;
  --grad:linear-gradient(90deg,var(--green),var(--blue));
}
*{margin:0;padding:0;box-sizing:border-box}
html,body{width:1200px;height:4241px;overflow:hidden;background:#fff}
body{position:relative;font-family:"Roboto",sans-serif;color:var(--text)}
.abs{position:absolute}
.center{text-align:center;left:0;width:1200px}
.btn{position:absolute;display:flex;align-items:center;justify-content:center;border-radius:26px;color:#fff;font-weight:500;font-size:16px;background:var(--grad)}
.btn.blue-first{background:linear-gradient(90deg,var(--blue),var(--green))}

/* header */
.contact-chip{position:absolute;top:30px;display:flex;align-items:center;gap:16px}
.chip-icon{width:46px;height:46px;border-radius:50%;background:var(--grad);display:flex;align-items:center;justify-content:center;flex:none}
.chip-label{font-size:11px;font-weight:500;color:#444}
.chip-value{font-size:18px;font-weight:700;color:var(--ink);margin-top:4px;white-space:nowrap}
.brand{position:absolute;display:flex;align-items:center;gap:12px;font-family:"Krona One",sans-serif;font-size:20px;line-height:25px;white-space:nowrap}
.brand-dot{width:38px;height:38px;border-radius:50%;background:var(--grad);flex:none}
.nav{position:absolute;left:110px;top:120px;width:980px;height:51px;border-radius:26px;background:var(--grad);display:flex;align-items:center;padding-left:44px;z-index:3}
.nav a{color:#fff;font-size:16px;font-weight:500;text-decoration:none;margin-right:52px}
.lang{position:absolute;right:58px;top:11px;width:70px;height:29px;border-radius:15px;background:#fff;color:var(--blue);font-size:11px;font-weight:700;display:flex;align-items:center;justify-content:center}
.nav-dot{position:absolute;right:10px;top:12px;width:28px;height:28px;border-radius:50%;background:var(--green);border:3px solid #fff}

/* hero */
.hero-photo{position:absolute;left:0;top:146px;width:1200px;height:610px;background:linear-gradient(180deg,#4e5a68 0%,#7a6a55 35%,#3a3c3e 60%,#26282b 100%)}
.hero-photo::after{content:"";position:absolute;inset:0;background:rgba(10,18,30,.35)}
.hero-kicker{top:266px;font-size:18px;font-weight:500;color:var(--green)}
.hero-title{top:302px;font-size:48px;color:#fff;font-family:"Krona One",sans-serif}
.hero-sub{top:370px;color:#fff;font-family:"Krona One",sans-serif;font-size:21px}
.hero-text{top:416px;left:320px;width:560px;text-align:center;color:#fff;font-size:17px;line-height:28px}
.btn-ghost{position:absolute;border:2px solid var(--green);color:var(--green);border-radius:26px;display:flex;align-items:center;justify-content:center;font-size:16px;font-weight:500}

/* about */
.about-ring{position:absolute;left:90px;top:785px;width:544px;height:544px;border-radius:50%;background:radial-gradient(circle,#e7efff 60%,#f5f8ff 100%)}
.about-photo{position:absolute;left:127px;top:822px;width:470px;height:470px;border-radius:50%;background:linear-gradient(160deg,#e8ecef,#c9ced3 55%,#2d333d)}
.section-title{font-family:"Krona One",sans-serif;color:var(--ink);font-size:36px;font-weight:400}
.about-copy{position:absolute;left:662px;top:918px;width:428px;font-size:15.5px;line-height:31.5px;text-align:justify}

/* stats */
.stat{position:absolute;width:220px;text-align:center;top:1552px}
.stat-num{font-family:"Krona One",sans-serif;font-size:48px;color:var(--blue)}
.stat-label{font-size:17px;margin-top:6px}

/* services */
.hex{position:absolute;width:184px;height:184px;clip-path:polygon(50% 0,100% 25%,100% 75%,50% 100%,0 75%,0 25%);background:#fff;display:flex;flex-direction:column;align-items:center;padding-top:28px}
.hex-label{font-size:15px;line-height:23px;text-align:center;color:#555;margin-top:16px}
.hex.active .hex-inner{position:absolute;inset:2px;clip-path:polygon(50% 0,100% 25%,100% 75%,50% 100%,0 75%,0 25%);background:linear-gradient(135deg,#1f9d7a,#0a5ee0)}
.hex.active .hex-content{position:relative;display:flex;flex-direction:column;align-items:center}
.hex.active .hex-label{color:#fff}

/* challenge */
.ticks{position:absolute;left:148px;top:2910px;list-style:none}
.ticks li{display:flex;align-items:center;gap:18px;font-size:15.5px;height:32px}
.team-photo{position:absolute;left:608px;top:2636px;width:480px;height:480px;border-radius:50%;border:3px solid var(--green);background:linear-gradient(150deg,#d9d4c9,#a7a196 45%,#c79a62 80%,#8a6a45);box-shadow:0 20px 50px rgba(0,0,0,.12)}

/* form */
.field{position:absolute;left:227px;width:359px;height:50px;border-radius:25px;background:var(--field);display:flex;align-items:center;padding-left:34px;gap:16px;font-size:12px;color:#555;letter-spacing:.5px}
.comments{position:absolute;left:614px;top:3407px;width:357px;height:270px;border-radius:24px;background:var(--field);padding:26px 34px;display:flex;gap:14px;align-items:flex-start;font-size:12px;color:#555;letter-spacing:.5px}

/* footer */
.footer{position:absolute;left:0;top:3712px;width:1200px;height:529px;background:var(--navy)}
.foot-head{position:absolute;font-family:"Krona One",sans-serif;font-size:15px;color:var(--green);white-space:nowrap}
.foot-list{position:absolute;list-style:none;color:#fff;font-size:15px}
.foot-list li{display:flex;align-items:flex-start;gap:20px;height:33.5px;white-space:nowrap}
.social{position:absolute;top:3931px;width:38px;height:38px;border-radius:50%;background:var(--green)}
</style>
</head>
<body>

<!-- header -->
<div class="contact-chip" style="left:110px">
  <div class="chip-icon"><svg width="20" height="20" viewBox="0 0 24 24" fill="#fff"><path d="M6.6 10.8a15.1 15.1 0 0 0 6.6 6.6l2.2-2.2c.3-.3.7-.4 1-.2 1.1.4 2.3.6 3.6.6.6 0 1 .4 1 1V20c0 .6-.4 1-1 1A17 17 0 0 1 3 4c0-.6.4-1 1-1h3.5c.6 0 1 .4 1 1 0 1.3.2 2.5.6 3.6.1.3 0 .7-.2 1z"/></svg></div>
  <div><div class="chip-label">CALL US:</div><div class="chip-value">+49 3000 555 010</div></div>
</div>
<div class="brand" style="left:462px;top:28px;color:var(--ink)"><span class="brand-dot"></span><span>Velmora<br>Systems GmbH</span></div>
<div class="contact-chip" style="left:790px">
  <div class="chip-icon"><svg width="20" height="20" viewBox="0 0 24 24" fill="none" stroke="#fff" stroke-width="2"><rect x="3" y="5" width="18" height="14" rx="2"/><path d="M3 7l9 6 9-6"/></svg></div>
  <div><div class="chip-label">EMAIL US:</div><div class="chip-value" style="font-size:14.5px">INFO@BRIGHT-HARBOR.EXAMPLE</div></div>
</div>

<nav class="nav">
  <a>HOME</a><a>ABOUT VS</a><a>SERVICES</a><a>CAREER</a><a>JOBS</a><a>GALLERY</a><a>CONTACT US</a>
  <span class="lang">ENG ⇕</span><span class="nav-dot"></span>
</nav>

<!-- hero -->
<div class="hero-photo" role="img" aria-label="Evening city riverside with a domed government building"></div>
<div class="abs center hero-kicker">VELMORA SYSTEMS GMBH</div>
<div class="abs center hero-title">GLOBAL EXCELLENCE</div>
<div class="abs center hero-sub">IN SOFTWARE QUALITY</div>
<p class="abs hero-text">We offer testing, consulting, and automation – ensuring digital products function reliably worldwide.</p>
<div class="btn blue-first" style="left:393px;top:490px;width:198px;height:50px">Request a Quote</div>
<div class="btn-ghost" style="left:607px;top:490px;width:198px;height:50px">Get Started Now</div>
<svg class="abs" style="left:0;top:640px" width="1200" height="120" viewBox="0 640 1200 120">
  <defs><linearGradient id="g1" x1="0" x2="1"><stop offset="0" stop-color="#3fe21e"/><stop offset="1" stop-color="#0a55e6"/></linearGradient></defs>
  <polygon points="110,738 600,654 1090,738 1090,754 600,670 110,754" fill="url(#g1)"/>
  <polygon points="0,760 0,756 110,756 110,754 600,670 1090,754 1090,756 1200,756 1200,760" fill="#fff"/>
</svg>

<!-- about -->
<div class="about-ring"></div>
<div class="about-photo" role="img" aria-label="Team of six colleagues holding a certificate in the office"></div>
<h2 class="abs section-title" style="left:662px;top:858px">ABOUT US</h2>
<div class="about-copy">
  <p>Our company philosophy is oriented toward the needs of the current IT landscape, taking future-oriented technologies into account. And we do so with a solution-oriented approach.</p>
  <p style="margin-top:32px">This factor is too important not to emphasize again here. What we offer? Comprehensive consulting from strategic orientation to implementation.</p>
</div>
<div class="btn blue-first" style="left:662px;top:1200px;width:171px;height:50px">Explore More</div>

<!-- grow -->
<h2 class="abs center section-title" style="top:1410px">COME AND GROW WITH US!</h2>
<p class="abs" style="left:250px;top:1462px;width:700px;text-align:center;font-size:16.5px;line-height:30px">There are plenty of reasons for this: responsible tasks, the joy of good work and unique career paths are just a fraction of them.</p>
<div class="stat" style="left:275px"><div class="stat-num">18</div><div class="stat-label">Successful years</div></div>
<div class="stat" style="left:490px"><div class="stat-num">07</div><div class="stat-label">Various Disciplines</div></div>
<div class="stat" style="left:704px"><div class="stat-num">10</div><div class="stat-label">Great Colleagues</div></div>

<!-- services -->
<svg class="abs" style="left:0;top:1660px" width="1200" height="880" viewBox="0 1660 1200 880">
  <defs>
    <linearGradient id="g2" x1="0" y1="0" x2="1" y2="0.4"><stop offset="0" stop-color="#3fe21e"/><stop offset=".55" stop-color="#1aa07a"/><stop offset="1" stop-color="#0a55e6"/></linearGradient>
  </defs>
  <rect x="0" y="1682" width="1200" height="833" fill="url(#g2)"/>
  <polygon points="0,1660 1200,1660 1200,1682 600,1782 0,1682" fill="#fff"/>
  <polygon points="110,1682 600,1764 1090,1682 1090,1702 600,1784 110,1702" fill="#0b1a3a"/>
  <polygon points="0,2540 1200,2540 1200,2515 600,2420 0,2515" fill="#fff"/>
  <polygon points="110,2495 600,2400 1090,2495 1090,2517 600,2422 110,2517" fill="#0b1a3a"/>
</svg>
<h2 class="abs center section-title" style="top:1856px;color:#fff">SERVICES WE OFFER</h2>
<p class="abs" style="left:250px;top:1907px;width:700px;text-align:center;font-size:16.5px;line-height:30px;color:#fff">We test your software! This helps you get the best possible business value from your IT systems. And we do it with passion!</p>

<svg width="0" height="0" style="position:absolute">
  <defs>
    <symbol id="hexicon" viewBox="0 0 62 62">
      <polygon points="31,2 57,16 57,46 31,60 5,46 5,16" fill="#0a55e6"/>
      <circle cx="31" cy="29" r="9" fill="none" stroke="#fff" stroke-width="2"/>
      <path d="M22 42h18M31 20v-4M31 38v4" stroke="#fff" stroke-width="2"/>
    </symbol>
  </defs>
</svg>

<div class="hex" style="left:110px;top:1998px"><svg width="62" height="62"><use href="#hexicon"/></svg><div class="hex-label">Testmanagement<br>Services</div></div>
<div class="hex" style="left:310px;top:1998px"><svg width="62" height="62"><use href="#hexicon"/></svg><div class="hex-label">Managed Testing<br>Services</div></div>
<div class="hex active" style="left:508px;top:1998px"><div class="hex-inner"></div><div class="hex-content"><svg width="62" height="62" viewBox="0 0 62 62"><polygon points="31,2 57,16 57,46 31,60 5,46 5,16" fill="#fff"/><circle cx="31" cy="29" r="9" fill="none" stroke="#1a9b6f" stroke-width="2"/><path d="M22 42h18" stroke="#1a9b6f" stroke-width="2"/></svg><div class="hex-label">Integration<br>Services</div></div></div>
<div class="hex" style="left:706px;top:1998px"><svg width="62" height="62"><use href="#hexicon"/></svg><div class="hex-label">Project &amp; Release<br>Management</div></div>
<div class="hex" style="left:905px;top:1998px"><svg width="62" height="62"><use href="#hexicon"/></svg><div class="hex-label">Development &amp;<br>Digitalization</div></div>

<div class="hex" style="left:211px;top:2170px"><svg width="62" height="62"><use href="#hexicon"/></svg><div class="hex-label">Highend Test<br>Automation Services</div></div>
<div class="hex" style="left:409px;top:2170px"><svg width="62" height="62"><use href="#hexicon"/></svg><div class="hex-label">Agile Testing<br>Services</div></div>
<div class="hex" style="left:608px;top:2170px"><svg width="62" height="62"><use href="#hexicon"/></svg><div class="hex-label">Business Consulting<br>Services</div></div>
<div class="hex" style="left:806px;top:2170px"><svg width="62" height="62"><use href="#hexicon"/></svg><div class="hex-label">Mobile Testing<br>Services</div></div>

<!-- challenge -->
<h2 class="abs section-title" style="left:110px;top:2636px;font-size:29px;line-height:51px;width:480px;white-space:nowrap">ARE YOU<br>LOOKING FOR A NEW<br>CHALLENGE?</h2>
<p class="abs" style="left:110px;top:2798px;width:440px;font-size:15.5px;line-height:31.5px">Would you like to experience us up close? Then the BrightHarbor team looks forward to meeting you at one of the following dates. We look forward to seeing you.</p>
<ul class="ticks">
  <li><svg width="16" height="16" viewBox="0 0 16 16"><rect x="1" y="1" width="14" height="14" rx="2" fill="none" stroke="#0a55e6" stroke-width="1.6"/><path d="M4 8l3 3 7-8" fill="none" stroke="#0a55e6" stroke-width="2"/></svg>Working Student Social Media (m/f/d)</li>
  <li><svg width="16" height="16" viewBox="0 0 16 16"><rect x="1" y="1" width="14" height="14" rx="2" fill="none" stroke="#0a55e6" stroke-width="1.6"/><path d="M4 8l3 3 7-8" fill="none" stroke="#0a55e6" stroke-width="2"/></svg>Test Automation Engineer (m/f/d)</li>
  <li><svg width="16" height="16" viewBox="0 0 16 16"><rect x="1" y="1" width="14" height="14" rx="2" fill="none" stroke="#0a55e6" stroke-width="1.6"/><path d="M4 8l3 3 7-8" fill="none" stroke="#0a55e6" stroke-width="2"/></svg>Test Manager (m/f/d)</li>
  <li><svg width="16" height="16" viewBox="0 0 16 16"><rect x="1" y="1" width="14" height="14" rx="2" fill="none" stroke="#0a55e6" stroke-width="1.6"/><path d="M4 8l3 3 7-8" fill="none" stroke="#0a55e6" stroke-width="2"/></svg>Working Student Graphic / Media Design (m/f/d)</li>
</ul>
<div class="btn blue-first" style="left:110px;top:3060px;width:171px;height:50px">Explore More</div>
<div class="team-photo" role="img" aria-label="Colleagues working on laptops at a wooden office desk"></div>

<!-- contact -->
<h2 class="abs center section-title" style="top:3250px">GET IN TOUCH WITH US</h2>
<p class="abs" style="left:240px;top:3303px;width:720px;text-align:center;font-size:16.5px;line-height:30px">I must explain to you how all this mistaken idea of denouncing pleasure and praising pain was born and I will give you a complete account of the system.</p>
<div class="field" style="top:3407px"><svg width="12" height="12" viewBox="0 0 12 12" fill="#666"><circle cx="6" cy="3.5" r="3"/><path d="M0 12c0-4 3-5 6-5s6 1 6 5z"/></svg>FULL NAME</div>
<div class="field" style="top:3480px"><svg width="14" height="11" viewBox="0 0 14 11" fill="#666"><rect width="14" height="11" rx="1"/><path d="M1 1l6 5 6-5" stroke="#efeff1" fill="none"/></svg>EMAIL ADDRESS</div>
<div class="field" style="top:3554px"><svg width="12" height="12" viewBox="0 0 24 24" fill="#666"><path d="M6.6 10.8a15.1 15.1 0 0 0 6.6 6.6l2.2-2.2c.3-.3.7-.4 1-.2 1.1.4 2.3.6 3.6.6.6 0 1 .4 1 1V20c0 .6-.4 1-1 1A17 17 0 0 1 3 4c0-.6.4-1 1-1h3.5c.6 0 1 .4 1 1 0 1.3.2 2.5.6 3.6.1.3 0 .7-.2 1z"/></svg>CONTACT NUMBER</div>
<div class="btn" style="left:227px;top:3626px;width:359px;height:51px;font-size:14px">SEND MESSAGE</div>
<div class="comments"><svg width="14" height="12" viewBox="0 0 14 12" fill="none" stroke="#666" stroke-width="1.4"><path d="M2 1h10v7H6l-3 3V8H2z"/></svg>COMMENTS</div>

<!-- footer -->
<footer class="footer"></footer>
<svg class="abs" style="left:0;top:3712px" width="1200" height="160" viewBox="0 3712 1200 160">
  <defs><linearGradient id="g3" x1="0" x2="1"><stop offset="0" stop-color="#3fe21e"/><stop offset="1" stop-color="#0a55e6"/></linearGradient></defs>
  <polygon points="110,3712 1090,3712 1090,3742 600,3840 110,3742" fill="#fff"/>
  <polygon points="110,3742 600,3840 1090,3742 1090,3758 600,3856 110,3758" fill="url(#g3)"/>
</svg>
<div class="brand" style="left:110px;top:3932px;color:#fff;font-size:18px;line-height:23px"><span class="brand-dot"></span><span>Velmora<br>Systems GmbH</span></div>

<div class="foot-head" style="left:472px;top:3930px">QUICK LINKS</div>
<ul class="foot-list" style="left:472px;top:3971px">
  <li><svg width="14" height="14" viewBox="0 0 14 14"><circle cx="7" cy="7" r="7" fill="#fff"/><path d="M6 4l3 3-3 3" stroke="#0b1a3a" stroke-width="1.8" fill="none"/></svg>Home</li>
  <li><svg width="14" height="14" viewBox="0 0 14 14"><circle cx="7" cy="7" r="7" fill="#fff"/><path d="M6 4l3 3-3 3" stroke="#0b1a3a" stroke-width="1.8" fill="none"/></svg>Who we are</li>
  <li><svg width="14" height="14" viewBox="0 0 14 14"><circle cx="7" cy="7" r="7" fill="#fff"/><path d="M6 4l3 3-3 3" stroke="#0b1a3a" stroke-width="1.8" fill="none"/></svg>Services</li>
  <li><svg width="14" height="14" viewBox="0 0 14 14"><circle cx="7" cy="7" r="7" fill="#fff"/><path d="M6 4l3 3-3 3" stroke="#0b1a3a" stroke-width="1.8" fill="none"/></svg>Our solutions</li>
  <li><svg width="14" height="14" viewBox="0 0 14 14"><circle cx="7" cy="7" r="7" fill="#fff"/><path d="M6 4l3 3-3 3" stroke="#0b1a3a" stroke-width="1.8" fill="none"/></svg>Contact Us</li>
</ul>

<div class="foot-head" style="left:690px;top:3930px">CONTACT INFO</div>
<ul class="foot-list" style="left:690px;top:3971px">
  <li style="height:67px;line-height:33.5px"><svg width="12" height="14" viewBox="0 0 12 16" fill="#fff" style="margin-top:9px"><path d="M6 0a6 6 0 0 0-6 6c0 4.5 6 10 6 10s6-5.5 6-10a6 6 0 0 0-6-6zm0 8.5A2.5 2.5 0 1 1 6 3.5a2.5 2.5 0 0 1 0 5z"/></svg><span style="margin-top:-8px">Lindenhang 7, Musterstadt,<br>Germany</span></li>
  <li><svg width="14" height="11" viewBox="0 0 14 11" fill="#fff"><rect width="14" height="11" rx="1"/><path d="M1 1l6 5 6-5" stroke="#0b1a3a" fill="none"/></svg>info@bright-harbor.example</li>
  <li><svg width="13" height="13" viewBox="0 0 24 24" fill="#fff"><path d="M6.6 10.8a15.1 15.1 0 0 0 6.6 6.6l2.2-2.2c.3-.3.7-.4 1-.2 1.1.4 2.3.6 3.6.6.6 0 1 .4 1 1V20c0 .6-.4 1-1 1A17 17 0 0 1 3 4c0-.6.4-1 1-1h3.5c.6 0 1 .4 1 1 0 1.3.2 2.5.6 3.6.1.3 0 .7-.2 1z"/></svg>+49 3000 5550101</li>
</ul>

<span class="social" style="left:959px"></span>
<span class="social" style="left:1003px"></span>
<span class="social" style="left:1049px"></span>

<div class="abs" style="left:110px;top:4170px;width:980px;height:1px;background:rgba(255,255,255,.25)"></div>
<div class="abs center" style="top:4194px;color:#fff;font-size:15px">(C) Copyright 2025 | All Rights Reserved</div>

</body>
</html>
```